Design Shopify E-Commerce Website for Men's Products

Design a Shopify website for men to sell our men's jewelry, cigar and bar accessories, and other men's products. Design should be hip, with like a rock n' roll, biker, whiskey driker flare. Name of the company is "Outlaw Cupboard" and website will be www.OutlawCupboard.com
Homepage will have navigation bar with three categories: Men's Jewelry, Cigar & Bar Products, Man Cave Swag
I will upload our logo, inspiration type pictures and some of the products that we sell
Theme colors should be mainly dark: black, grey, brown, gold

```html
<!DOCTYPE html>
<html lang="en">
<head>
<meta charset="utf-8">
<title>Outlaw Cupboard</title>
<link href="https://fonts.googleapis.com/css2?family=Poppins:wght@300;400;500;600;800;900&display=swap" rel="stylesheet">
<style>
:root{
  --black:#000;
  --gold:#f5b100;
  --white:#fff;
  --brown:#7a5842;
  --brown-dark:#573a2c;
  --grey:#2a2a2a;
}
*{margin:0;padding:0;box-sizing:border-box}
html,body{width:1200px;height:3833px;overflow:hidden;background:var(--black)}
body{position:relative;font-family:'Poppins',sans-serif;color:var(--white)}
.abs{position:absolute}
.nav a{position:absolute;top:42px;font-size:15px;color:var(--white);text-decoration:none;transform:translateX(-50%);white-space:nowrap}
.brand{position:absolute;top:18px;left:600px;transform:translateX(-50%);display:flex;align-items:center;gap:8px;font-size:16px;font-weight:600;color:var(--gold);white-space:nowrap}
.brand .dot{width:14px;height:14px;border-radius:50%;background:var(--gold)}
.hero-photo{position:absolute;left:560px;top:90px;width:640px;height:660px;background:radial-gradient(ellipse at 55% 40%,#4a4540 0%,#1f1d1c 45%,#000 80%)}
.hero-text{position:absolute;left:110px;top:196px}
.welcome{font-size:44px;font-weight:300;line-height:1.2}
.title{font-size:62px;font-weight:800;line-height:1.2;margin-top:6px}
.lead{font-size:21px;line-height:34px;margin-top:10px;width:700px}
.btn{position:absolute;width:179px;height:55px;border:2px solid var(--white);display:flex;align-items:center;justify-content:center;gap:14px;font-size:17px;font-weight:600;color:var(--white)}
.btn .arrow{width:27px;height:27px;border-radius:50%;background:var(--white);display:flex;align-items:center;justify-content:center}
.dots{position:absolute;left:600px;transform:translateX(-50%);display:flex;gap:12px}
.dots i{width:10px;height:10px;border-radius:50%;background:var(--white)}
.dots i.on{background:var(--gold)}
.section-title{position:absolute;left:600px;transform:translateX(-50%);font-size:32px;font-weight:800;white-space:nowrap}
.section-title span{color:var(--gold)}
.photo{position:absolute}
.about-frame{position:absolute;left:128px;top:767px;width:456px;height:402px;border:8px solid var(--gold)}
.about-title{position:absolute;left:631px;top:757px;font-size:32px;font-weight:800}
.about-title span{color:var(--gold)}
.about-copy{position:absolute;left:631px;top:822px;width:460px;font-size:15px;line-height:34.3px}
.cat-label{position:absolute;height:61px;background:#0d0d0d;display:flex;align-items:center;justify-content:center;font-size:19px;font-weight:800}
.cat-overlay{position:absolute;left:445px;top:1386px;width:310px;height:277px;display:flex;flex-direction:column;align-items:center;padding-top:32px;text-align:center;font-size:21px;line-height:34px;font-weight:300}
.cat-overlay b{font-weight:600;margin-top:12px}
.t-side{position:absolute;top:2855px;height:255px;background:var(--brown-dark)}
.t-card{position:absolute;left:278px;top:2814px;width:639px;height:296px;background:var(--brown)}
.t-side p,.t-card p{font-size:13px;line-height:28.5px}
.avatar{position:absolute;left:548px;top:2770px;width:104px;height:104px;border-radius:50%;background:linear-gradient(135deg,#5a3fa0,#2c2348)}
.t-quote{position:absolute;left:0;right:0;top:105px;text-align:center;padding:0 18px}
.t-name{font-size:17px !important;font-weight:600;margin-top:2px}
.t-role{font-size:13px !important;line-height:20px !important}
.quote-mark{font-size:72px;font-weight:900;color:var(--gold);line-height:1;height:40px;margin-top:-4px}
.footer-brand{position:absolute;left:600px;top:3430px;transform:translateX(-50%);display:flex;align-items:center;gap:14px;font-size:34px;font-weight:600;color:var(--gold);white-space:nowrap}
.footer-brand .dot{width:30px;height:30px;border-radius:50%;background:var(--gold)}
.footer-nav a{position:absolute;top:3605px;font-size:16px;color:var(--white);text-decoration:none;transform:translateX(-50%);white-space:nowrap}
.social{position:absolute;top:3675px;width:40px;height:40px;border-radius:50%;border:2px solid var(--white);transform:translateX(-50%)}
.copyright{position:absolute;top:3766px;left:600px;transform:translateX(-50%);font-size:15px;white-space:nowrap}
</style>
</head>
<body>

<header class="nav">
  <a href="#" style="left:177px">Home</a>
  <a href="#" style="left:268px">About Us</a>
  <a href="#" style="left:389px">Men's Jewelry</a>
  <div class="brand"><span class="dot"></span>Outlaw Cupboard</div>
  <a href="#" style="left:817px">Cigar&nbsp; Bar Products</a>
  <a href="#" style="left:986px">Man Cave Swag</a>
</header>

<div class="hero-photo" role="img" aria-label="Bearded man in sunglasses and leather jacket smoking a cigar"></div>

<section class="hero-text">
  <h2 class="welcome">Welcome To</h2>
  <h1 class="title">Outlaw Cupboard</h1>
  <p class="lead">Sed ut perspiciatis unde omnis iste natus error sit voluptatem accusantium doloremque laudantium</p>
</section>
<a class="btn" style="left:110px;top:444px;height:57px">Get Started <span class="arrow"><svg width="12" height="12" viewBox="0 0 12 12"><path d="M4 2l4 4-4 4" fill="none" stroke="#000" stroke-width="2"/></svg></span></a>
<div class="dots" style="top:535px"><i></i><i class="on"></i><i></i></div>

<svg class="abs" style="left:0;top:590px" width="1200" height="170" viewBox="0 590 1200 170">
  <path d="M0 747 Q600 470 1200 737 L1200 760 L0 760Z" fill="#000"/>
  <path d="M0 747 Q600 470 1200 737" fill="none" stroke="#f5b100" stroke-width="7"/>
</svg>

<!-- About -->
<div class="about-frame"></div>
<div class="photo" role="img" aria-label="Bearded man in leather jacket holding a bottle in a bar" style="left:137px;top:777px;width:456px;height:381px;background:radial-gradient(ellipse at 45% 40%,#3b4048,#1b1d22 60%,#0c0c0e)"></div>
<svg class="abs" style="left:530px;top:730px" width="80" height="50">
  <g stroke="#f5b100" stroke-width="6"><path d="M8 48 L50 6"/><path d="M22 48 L64 6"/><path d="M36 48 L78 6"/></g>
</svg>
<svg class="abs" style="left:100px;top:1160px" width="90" height="60">
  <g stroke="#f5b100" stroke-width="6"><path d="M4 48 L46 6"/><path d="M18 54 L60 12"/><path d="M32 58 L74 16"/><path d="M46 58 L86 18"/></g>
</svg>
<h2 class="about-title"><span>About</span> Us</h2>
<p class="about-copy">Lorem ipsum dolor sit amet, consectetur adipiscing elit, sed do eiusmod tempor incididunt ut labore et dolore magna aliqua. Quis ipsum suspendisse ultrices gravida. Risus commodo viverra maecenas accumsan lacus vel facilisis. incididunt ut labore et dolore magna aliqua. Quis ipsum suspendisse ultrices gravida. Risus commodo viverra maecenas accumsan lacus vel facilisis.</p>
<a class="btn" style="left:633px;top:1088px">Read More <span class="arrow"><svg width="12" height="12" viewBox="0 0 12 12"><path d="M4 2l4 4-4 4" fill="none" stroke="#000" stroke-width="2"/></svg></span></a>

<!-- Categories -->
<h2 class="section-title" style="top:1295px"><span>Our</span> Categories</h2>
<div class="photo" role="img" aria-label="Cigar beside a glass of whiskey on wood" style="left:112px;top:1386px;width:309px;height:277px;background:linear-gradient(135deg,#2a1a0e,#6b4020 55%,#3a2412)"></div>
<div class="photo" role="img" aria-label="Silver cufflinks on a wooden surface" style="left:445px;top:1386px;width:310px;height:277px;background:linear-gradient(135deg,#6e5a4a,#4a3a30 60%,#5c4a3c)"></div>
<div class="cat-overlay">Lorem ipsum dolor sit amet, consectetur adipiscing elit, sed do eiusip<b>$50</b></div>
<div class="photo" role="img" aria-label="Black and white chrome motorcycles" style="left:779px;top:1386px;width:309px;height:277px;background:linear-gradient(135deg,#d8d8d8,#3a3a3a 50%,#bdbdbd)"></div>
<div class="cat-label" style="left:112px;top:1663px;width:309px">Cigar &amp; Bar Products</div>
<div class="cat-label" style="left:445px;top:1663px;width:310px">Men's Jewelry</div>
<div class="cat-label" style="left:779px;top:1663px;width:309px">Man Cave Swag</div>
<a class="btn" style="left:521px;top:1750px;height:54px">Shop Now <span class="arrow"><svg width="12" height="12" viewBox="0 0 12 12"><path d="M4 2l4 4-4 4" fill="none" stroke="#000" stroke-width="2"/></svg></span></a>
<div class="dots" style="top:1840px"><i></i><i class="on"></i><i></i></div>

<!-- Gallery -->
<h2 class="section-title" style="top:1932px"><span>Our</span> Gallery</h2>
<div class="photo" role="img" aria-label="Cigar and whiskey glass on a wooden table" style="left:112px;top:2025px;width:351px;height:469px;background:linear-gradient(135deg,#2a1a0e,#6b4020 55%,#3a2412)"></div>
<div class="photo" role="img" aria-label="Wooden cigar cutter with cigars" style="left:470px;top:2025px;width:243px;height:225px;background:linear-gradient(135deg,#e6d2b8,#8a4e28 55%,#d9c5ae)"></div>
<div class="photo" role="img" aria-label="Cufflinks on wood" style="left:470px;top:2260px;width:243px;height:235px;background:linear-gradient(135deg,#7a6250,#4e3e32 60%,#6c5646)"></div>
<div class="photo" role="img" aria-label="Black and white motorcycles" style="left:719px;top:2025px;width:369px;height:469px;background:linear-gradient(135deg,#e0e0e0,#2c2c2c 50%,#c8c8c8)"></div>
<a class="btn" style="left:511px;top:2543px;height:54px">See More <span class="arrow"><svg width="12" height="12" viewBox="0 0 12 12"><path d="M4 2l4 4-4 4" fill="none" stroke="#000" stroke-width="2"/></svg></span></a>

<!-- Testimonials -->
<h2 class="section-title" style="top:2680px"><span>Client</span> Testimonials</h2>
<div class="t-side" style="left:112px;width:180px;overflow:hidden"><p style="position:absolute;left:12px;top:66px;width:400px">Lorem ipsum dolor sit amet<br>labore et dolore magna aliqua</p></div>
<div class="t-side" style="left:905px;width:183px;overflow:hidden"><p style="position:absolute;right:8px;top:66px;width:400px;text-align:right">od tempor incididunt ut<br>a. Risus commodo viverra</p></div>
<div class="t-card">
  <div class="t-quote">
    <p>Lorem ipsum dolor sit amet, consectetur adipiscing elit, sed do eiusmod tempor incididunt ut labore et dolore magna aliqua. Quis ipsum suspendisse ultrices gravida. Risus commodo viverra maecenas accumsan lacus vel facilisis.</p>
    <p class="t-name">Daniel Marsh</p>
    <p class="t-role">Lorem Ipsum</p>
    <div class="quote-mark">”</div>
  </div>
</div>
<div class="avatar" role="img" aria-label="Client portrait"></div>
<div class="dots" style="top:3177px"><i></i><i class="on"></i><i></i></div>

<!-- Footer -->
<svg class="abs" style="left:0;top:3260px" width="1200" height="180" viewBox="0 3260 1200 180">
  <path d="M0 3414 Q600 3140 1200 3425" fill="none" stroke="#f5b100" stroke-width="7"/>
</svg>
<div class="footer-brand"><span class="dot"></span>Outlaw Cupboard</div>
<nav class="footer-nav">
  <a href="#" style="left:308px">Home</a>
  <a href="#" style="left:400px">About Us</a>
  <a href="#" style="left:521px">Men's Jewelry</a>
  <a href="#" style="left:682px">Cigar&nbsp; Bar Products</a>
  <a href="#" style="left:852px">Man Cave Swag</a>
</nav>
<span class="social" style="left:512px" aria-label="Social link 1"></span>
<span class="social" style="left:576px" aria-label="Social link 2"></span>
<span class="social" style="left:634px" aria-label="Social link 3"></span>
<span class="social" style="left:694px" aria-label="Social link 4"></span>
<p class="copyright">© 2023 OutlawCupboard | All Rights Reserved</p>

</body>
</html>
```